Construction company focused on concrete and shed construction.

We need to update our current business card for ridgeforgebuilds.com.au we would like an eye catching design with blue, grey and white incorporating our current logo.
Our company started off in concreting and due to varying factors we have expanded to include shed construction as well.
This has led to our current Logo looking a little out of place and somehow need to use the card to bring in the shed construction side of the business while not having to change current concrete look "KESTRO" logo as we already have this incorporated into our company clothing and are not willing to change this yet.
Photo image attached for inspiration/ visual reference of type of work, not to be used on final design.
Please no cheesy designs of men in hard hats and tools
Final design should demonstrate a modern and service focused company.

Target Market(s)

Farmers, Business owners, Developers, Architects, Commercial project delivery

Industry/Entity Type

Construction Company

Contact Information for Business Card

Kestro Constructions.
7b Harlow st
South Launceston Tas
03 62918873

Font styles to use
Other font styles liked:
• see font in logo

Colors
3176b5
b2b2b2

Requirements
Must have
• Easy to read font,
• good contrast between back ground and writing
Nice to have
• Modern and corporate look with a fun but professional image.
Should not have
• Comic images or shadow images of tools/ people.

```html
<!DOCTYPE html>
<html lang="en">
<head>
<meta charset="utf-8">
<title>Kestro Constructions – Business Card</title>
<link rel="stylesheet" href="https://fonts.googleapis.com/css2?family=Roboto:wght@400;500&family=Roboto+Condensed:wght@700&display=swap">
<style>
  :root {
    --backdrop: #2a2a2a;
    --card: #f2f2f2;
    --brand-blue: #1f5b95;
    --ink: #444444;
    --rule: #555555;
    --rule-light: #b2b2b2;
  }
  * { box-sizing: border-box; margin: 0; padding: 0; }
  html, body { width: 1200px; height: 960px; overflow: hidden; }
  body {
    position: relative;
    background: var(--backdrop);
    font-family: "Roboto", Arial, sans-serif;
    color: var(--ink);
  }
  .card {
    position: absolute;
    width: 600px;
    height: 342px;
    background: var(--card);
    border-radius: 22px;
  }
  .card--front { left: 314px; top: 113px; }
  .card--back { left: 311px; top: 472px; }

  .brand-mark {
    position: absolute;
    display: flex;
    align-items: center;
    gap: 10px;
  }
  .brand-mark__dot {
    border-radius: 50%;
    background: var(--brand-blue);
  }
  .brand-mark__name {
    font-family: "Roboto Condensed", Arial, sans-serif;
    font-weight: 700;
    color: var(--brand-blue);
    letter-spacing: 1px;
  }

  .card--front .brand-mark { left: 0; right: 0; top: 62px; justify-content: center; }
  .card--front .brand-mark__dot { width: 26px; height: 26px; }
  .card--front .brand-mark__name { font-size: 30px; }

  .rule {
    position: absolute;
    left: 38px;
    width: 526px;
    height: 1px;
    background: var(--rule);
  }
  .rule--top { top: 152px; }
  .rule--bottom { top: 209px; }

  .holder {
    position: absolute;
    top: 158px;
    left: 0; right: 0;
    text-align: center;
  }
  .holder__name {
    font-family: "Roboto Condensed", Arial, sans-serif;
    font-weight: 700;
    font-size: 21px;
    line-height: 26px;
    color: var(--brand-blue);
  }
  .holder__role {
    font-weight: 500;
    font-size: 15px;
    line-height: 18px;
    color: var(--ink);
  }

  .contact {
    position: absolute;
    top: 233px;
    left: 0; right: 0;
    text-align: center;
    font-size: 14.5px;
    line-height: 18px;
  }
  .contact__lines { margin-top: 8px; }
  .contact__label { font-weight: 500; color: var(--brand-blue); }

  .card--back .brand-mark { left: 146px; top: 118px; gap: 16px; }
  .card--back .brand-mark__dot { width: 92px; height: 92px; }
  .group-name {
    border-top: 1px solid var(--rule-light);
    border-bottom: 1px solid var(--rule-light);
    padding: 2px 2px 1px;
  }
  .card--back .brand-mark__name { font-size: 28px; line-height: 30px; }

  .card__web {
    position: absolute;
    top: 288px;
    left: 0; right: 0;
    text-align: center;
    font-size: 14.5px;
  }
</style>
</head>
<body>
  <section class="card card--front">
    <div class="brand-mark">
      <span class="brand-mark__dot"></span>
      <span class="brand-mark__name">KESTRO</span>
    </div>
    <div class="rule rule--top"></div>
    <div class="holder">
      <p class="holder__name">DANIEL MARSH</p>
      <p class="holder__role">CEO/FOUNDER</p>
    </div>
    <div class="rule rule--bottom"></div>
    <div class="contact">
      <p>Kestro Constructions</p>
      <p>7b Harlow st, South Launceston Tas</p>
      <div class="contact__lines">
        <p><span class="contact__label">P:</span> 03 62918873 <span class="contact__label">E:</span> info@ridgeforgebuilds.com.au</p>
        <p><span class="contact__label">W:</span> ridgeforgebuilds.com.au</p>
      </div>
    </div>
  </section>

  <section class="card card--back">
    <div class="brand-mark">
      <span class="brand-mark__dot"></span>
      <span class="group-name"><span class="brand-mark__name">KESTRO GROUP</span></span>
    </div>
    <p class="card__web">www.ridgeforgebuilds.com.au</p>
  </section>
</body>
</html>
```